Change of Address Card

We are fertility physicians in New York . Need a change of address postcard .

The front should be colorful
contain the statement " we are moving!"
and the names Lorenzo Bettuni MD, Oksana Dremova MD

Also the front should contain the drawing of a sperm with either wings or wheeels or whatever your creativity suggests as long as it is not vulgar ( we are doctors !)

The back should contain
the address area and stamp area
and a text area
and possibly a recall of the drawing in front.
use same font

text below

Dear Friends and Colleagues

Lorenzo and Oksana are relocating their fertility practice to a new location on 418 West 71st Street, Suite 604, New York NY 10023
Please take note of our new phone number
Our New phone Number is 212-555-0194

Thank you for your support!

Target Market(s)

this is a card that goes to physicians

Industry/Entity Type

It Support

Requirements
Must have
• fit standard postcard size
Rectangular
At least 3-1/2 inches high x 5 inches long x 0.007 inch thick
No more than 4-1/4 inches high x 6 inches long x 0.016 inches thick
will not be mailed in an envelope

```html
<!DOCTYPE html>
<html lang="en">
<head>
<meta charset="utf-8">
<title>Change of Address Postcard – Back</title>
<link rel="stylesheet" href="https://fonts.googleapis.com/css2?family=Jost:ital,wght@0,400;0,700;1,400&display=swap">
<style>
  :root {
    --blue-light: #00b4ff;
    --blue-deep: #0078ff;
    --egg-white: #ffffff;
    --ink: #111111;
    --accent-red: #ff0000;
    --panel-grey: #e6e7e9;
    --rule-grey: #b0b0b0;
    --sperm-grey: #c9c9d2;
  }
  html, body {
    margin: 0;
    padding: 0;
    overflow: hidden;
    background: #ffffff;
  }
  .postcard {
    position: relative;
    width: 1200px;
    height: 850px;
    overflow: hidden;
    font-family: "Jost", "Futura", sans-serif;
    color: var(--ink);
    background:
      radial-gradient(circle 490px at 701px 410px, var(--egg-white) 0, var(--egg-white) 94%, rgba(255,255,255,0) 100%),
      linear-gradient(90deg, var(--blue-light) 0, var(--blue-light) 160px, var(--blue-deep) 460px);
  }
  .message {
    position: absolute;
    left: 134px;
    top: 66px;
    width: 420px;
    font-size: 22px;
    line-height: 30px;
  }
  .message p { margin: 0; }
  .greeting { margin-bottom: 30px !important; }
  .new-address {
    margin-top: 18px !important;
    color: var(--accent-red);
    font-weight: 700;
    font-size: 28px;
    line-height: 36px;
  }
  .phone-note {
    position: absolute;
    left: 134px;
    top: 482px;
    font-size: 22px;
    line-height: 30px;
    margin: 0;
  }
  .new-phone {
    position: absolute;
    left: 134px;
    top: 558px;
    margin: 0;
    color: var(--accent-red);
    font-weight: 700;
    font-size: 28px;
    line-height: 36px;
  }
  .thanks {
    position: absolute;
    left: 134px;
    top: 632px;
    margin: 0;
    font-style: italic;
    font-size: 22px;
    line-height: 30px;
  }
  .sperm-motif {
    position: absolute;
    left: 0;
    top: 382px;
    width: 220px;
    height: 32px;
    border-radius: 0 16px 16px 0;
    background: linear-gradient(90deg, rgba(201,201,210,0) 0, rgba(201,201,210,0.5) 55%, var(--sperm-grey) 80%, #e2e2e8 100%);
  }
  .address-panel {
    position: absolute;
    left: 771px;
    top: 554px;
    width: 379px;
    height: 260px;
    background: var(--panel-grey);
  }
  .address-panel svg { display: block; }
</style>
</head>
<body>
  <main class="postcard">
    <div class="sperm-motif" role="img" aria-label="Illustration of a swimming sperm heading toward the egg"></div>

    <section class="message">
      <p class="greeting">Dear Friends and Colleagues,</p>
      <p>Lorenzo and Oksana are relocating<br>their fertility practice to a new loca-<br>tion on:</p>
      <p class="new-address">418 West 71st Street,<br>Suite 604,<br>New York NY 10023</p>
    </section>

    <p class="phone-note">Please take note of our new<br>phone number:</p>
    <p class="new-phone">212-555-0194</p>
    <p class="thanks">Thank you for your support!</p>

    <div class="address-panel" aria-label="Recipient address area">
      <svg width="379" height="260" viewBox="0 0 379 260" aria-hidden="true">
        <g stroke="var(--rule-grey)" stroke-width="2">
          <line x1="36" y1="35" x2="326" y2="35"/>
          <line x1="36" y1="80" x2="326" y2="80"/>
          <line x1="36" y1="125" x2="326" y2="125"/>
          <line x1="36" y1="170" x2="326" y2="170"/>
          <line x1="36" y1="214" x2="326" y2="214"/>
        </g>
      </svg>
    </div>
  </main>
</body>
</html>
```